Website/Logo Design

We need a logo and website design for an opinion mining startup called VantroLux. Our technology mines the web to automatically discover what people are saying about brands, products, etc. The project we are fielding here is for our informational, public-facing website. In its initial incarnation, it will simply be a vehicle for marketing materials and information on our company and its offerings, but it should be flexible enough to expand as more content/functionality is added.

Some designs we like are:
http://www.brivel-nodo.com
http://www.tarnwisp.com
http://www.kvh.com
http://www.zellmorit.com
http://quontavel.com
http://marbiquex.com
http://www.vadup.com
Updates

All, please try to shy away from using a photo of a person as the focal point of the design.  Our company is more technological than social.

Target Market(s)

Primarily businesses interested in sentiment analysis (typically companies involved in advertising, market research, PR, etc.)

Industry/Entity Type

It Company

Requirements
Must have
• We are looking for a clean, modern, and professional design. This includes a logo, homepage, and internal page if it will differ from the homepage.
Nice to have
• It would be excellent if you could provide an HTML mockup if your design is chosen.
Should not have
• Flash, excessive bells and whistles

```html
<!DOCTYPE html>
<html lang="en">
<head>
<meta charset="utf-8">
<title>VantroLux</title>
<link rel="stylesheet" href="https://fonts.googleapis.com/css2?family=Noto+Sans:wght@400;700&family=Noto+Sans+Mono:wght@700&family=Questrial&display=swap">
<style>
:root{
  --ink:#111;
  --muted:#555;
  --rule:#444;
  --grey-text:#999;
  --teal:#1f6677;
  --link:#b0430f;
  --box-bg:#f7f7f7;
  --box-line:#999;
  --accent:#f47a7a;
  --demo:#f9c8a6;
  --arrow:#cfcfcf;
  --client:#444;
}
*{margin:0;padding:0;box-sizing:border-box}
html,body{width:1200px;height:1102px;overflow:hidden;background:#fff}
body{font-family:"Noto Sans",sans-serif;color:var(--ink)}
.page{position:relative;width:1200px;height:1102px;border:1px solid #333;background:#fff}
.abs{position:absolute;white-space:nowrap}
.social-links{left:700px;top:21px;width:134px;text-align:right;font-size:10px;color:#3f78a8}
.utility{top:18px;font-size:14px;color:var(--muted)}
.search{left:974px;top:17px;width:155px;height:24px;border:1px solid #999;background:#fff}
.search-btn{position:absolute;left:0;top:0;width:24px;height:22px;background:#c8c8c8;border-right:1px solid #999}
.brand{font-family:"Questrial",sans-serif;color:#222;letter-spacing:.5px}
.brand-main{left:72px;top:90px;font-size:30px}
.nav{left:223px;top:143px;width:750px;height:37px;border-top:1px solid var(--rule);border-bottom:1px solid var(--rule);
  background:repeating-linear-gradient(120deg,#fff 0 38px,#e6e6e6 38px 39px)}
.nav a{position:absolute;top:7px;font-size:15px;color:var(--ink);text-decoration:none}
.nav .current-bar{position:absolute;left:26px;top:22px;width:64px;height:13px;background:linear-gradient(#ffb0b0,var(--accent))}
.hero{left:222px;top:207px;width:758px;height:236px;border:3px solid #888;box-shadow:0 0 6px rgba(0,0,0,.35);background:#fff}
.hero-text{position:absolute;left:18px;top:26px;font-size:15px;line-height:15px;white-space:nowrap}
.hero-text small{display:block;font-size:11px;line-height:12px}
.hero-art{position:absolute;left:240px;top:4px;width:510px;height:224px;
  background:radial-gradient(ellipse at 30% 60%,#dbe6f2,#f4f6f9 60%,#fff)}
.tagline{left:245px;top:473px;font-family:"Noto Sans Mono",monospace;font-weight:700;font-size:16.5px;line-height:17px;color:var(--grey-text);letter-spacing:.35px}
.step{width:147px;height:147px;border:1px solid var(--box-line);border-radius:8px;background:var(--box-bg);padding:4px 5px;white-space:nowrap}
.step h3{font-weight:400;font-size:16.5px;line-height:16px;color:var(--teal);padding-left:6px}
.step p{font-size:12.5px;line-height:12.5px}
.step .more{display:block;font-size:10px;line-height:11px;color:var(--link)}
.demo{position:absolute;left:55px;top:106px;width:75px;height:23px;border:1px solid #a0504a;border-radius:4px;background:var(--demo);font-size:12px;text-align:center;line-height:21px}
.col-rule{top:760px;height:150px;border-left:1px dashed #555}
.col-head{font-size:16.5px}
.post-title{left:239px;top:800px;font-size:15px}
.meta{left:241px;top:820px;font-size:7.5px}
.body-s{font-size:11.5px;line-height:11.2px}
.video{left:426px;top:802px;width:118px;height:77px;border:1px solid #333;background:linear-gradient(#8fb3de,#c9d9ee)}
.clients{left:812px;top:806px;width:108px;font-size:8.5px;color:var(--client);display:grid;grid-template-columns:36px 36px 36px;row-gap:6px;line-height:12px}
.footer-rule{left:226px;top:962px;width:748px;border-top:1px solid var(--rule)}
.copyright{left:239px;top:979px;font-size:11px}
.brand-foot{left:826px;top:972px;font-size:21px}
</style>
</head>
<body>
<div class="page">
  <div class="abs social-links">Linkora · Chirpwell · Feedline</div>
  <a class="abs utility" style="left:848px">contact</a>
  <a class="abs utility" style="left:915px">login</a>
  <div class="abs search"><span class="search-btn"><svg width="24" height="22"><line x1="10" y1="11" x2="14" y2="15" stroke="#111" stroke-width="2"/></svg></span></div>

  <div class="abs brand brand-main">VantroLux</div>

  <nav class="abs nav">
    <span class="current-bar"></span>
    <a style="left:35px">Home</a>
    <a style="left:119px">services</a>
    <a style="left:229px">cases</a>
    <a style="left:320px">products</a>
    <a style="left:430px">blog</a>
    <a style="left:498px">about us</a>
  </nav>

  <section class="abs hero">
    <div class="hero-text">Pellentesque habitant morbi<br>tristique senectus et netus<br>et malesuada fames ac turpis<br>egestas.<small>Vestibulum tortor quam,</small></div>
    <div class="hero-art" role="img" aria-label="Illustration of social network icons around a central user, and a cycle diagram linking social marketing, consistent online communication, website and customers"></div>
  </section>

  <p class="abs tagline">Our company specializes Pellentesque habitant morbi tristique senectus<br>et netus et malesuada fames ac turpis egestas. Vestibulum tortor</p>

  <div class="abs step" style="left:310px;top:551px">
    <h3 style="margin:4px 0 15px">Social Media</h3>
    <p>People share their<br>opinions about<br>products and services<br>at social media</p>
    <a class="more">read more&gt;&gt;</a>
  </div>
  <svg class="abs" style="left:466px;top:616px" width="54" height="22"><g fill="var(--arrow)"><circle cx="5" cy="11" r="3"/><circle cx="15" cy="11" r="3"/><circle cx="25" cy="11" r="3"/></g><polyline points="40,3 48,11 40,19" fill="none" stroke="var(--arrow)" stroke-width="4"/></svg>
  <div class="abs step" style="left:527px;top:551px">
    <h3 style="margin:0 0 3px;padding-left:11px">Listen to your<br>customers</h3>
    <p>Listen / Follow social<br>conversations about<br>your product through<br>social media</p>
    <span class="demo">Try Demo</span>
  </div>
  <svg class="abs" style="left:682px;top:616px" width="54" height="22"><g fill="var(--arrow)"><circle cx="5" cy="11" r="3"/><circle cx="15" cy="11" r="3"/><circle cx="25" cy="11" r="3"/></g><polyline points="40,3 48,11 40,19" fill="none" stroke="var(--arrow)" stroke-width="4"/></svg>
  <div class="abs step" style="left:744px;top:553px">
    <h3 style="margin:4px 0 15px">Act accordingly</h3>
    <p>See how companies<br>took chance of social<br>media information<br>to manage their<br>strategic</p>
    <a class="more">case studies&gt;&gt;</a>
  </div>

  <div class="abs col-head" style="left:237px;top:758px">Latest post</div>
  <div class="abs post-title">Title entesque</div>
  <div class="abs meta">14/5 &nbsp;13:15pm &nbsp;category:marketing</div>
  <p class="abs body-s" style="left:240px;top:835px">Pellentesque habitant morbi<br>tristique senectus et netus<br>et malesuada fames ac turpis<br>egestas.<br>Vestibulum tortor quam,</p>

  <div class="abs col-rule" style="left:412px"></div>
  <div class="abs col-head" style="left:427px;top:758px">Latest video</div>
  <div class="abs video" role="img" aria-label="Video thumbnail with app icons and a play button"></div>
  <p class="abs body-s" style="left:420px;top:885px">Pellentesque habitant morbi<br>tristique senectus et netus</p>

  <div class="abs col-rule" style="left:598px"></div>
  <div class="abs col-head" style="left:606px;top:760px">message</div>
  <p class="abs body-s" style="left:604px;top:807px">Pellentesque habitant morbi<br>tristique senectus et netus<br>et malesuada fames ac turpis<br>egestas.<br>Vestibulum tortor quam,</p>

  <div class="abs col-rule" style="left:787px"></div>
  <div class="abs" style="left:808px;top:764px;font-size:13px">some of our clients</div>
  <div class="abs clients">
    <span>Orvia</span><span>Tessaly</span><span>Brindle</span>
    <span>Nomra</span><span>Kavo</span><span>Quell</span>
    <span>Pelto</span><span>Zarin</span><span>Fenn</span>
    <span>Umbra</span><span>Lisk</span><span>Dovan</span>
  </div>

  <div class="abs footer-rule"></div>
  <div class="abs copyright">Copyright ©2010 VantroLux</div>
  <div class="abs brand brand-foot">VantroLux</div>
</div>
</body>
</html>
```